20€ Frühlings-Rabatt: Spare jetzt bei Deinem Wettbewerb mit dem Gutscheincode: Mai24
ansprechende Grafik für Leistungserstellungsprozess (Wertstrom) eines Holzbauunternehmens - Infografiken
Zielgruppe
Wir sind ein Holzbauunternehmen mit knapp 100 Mitarbeitern. Unsere Zielgruppen sind öffentliche, gwerbliche und private Bauherren.
Internetseite: lindtal-holzhaus.de
Aufgabenstellung
Der Prozess vom Bauwunsch unserer Kunden bis zur letzten Mängelabnahme soll anschaulich dargestellt werden. Dazu soll aus den bereits vorhandenen, verschiedenen grafischen Darstellungen unseres Leistungserstellungsprozesses (d.h. unseres Wertstromes) eine ansprechende Grafik entwickelt werden. Siehe dazu den Entwurf als Handskizze in elliptischer Form.
Ebenso ist eine Orientierung an unserem Firmenlogo wünschenswert.
Siehe: www.lindtal-holzhaus.de
Die Grafik dient zur Erklärung, Erläuterung unserer wesentlichen Prozess-Schritte für folgende Zielgruppen:
Kunden, Besuchergruppen, vorhandene Mitarbeiter (interne Schulungen), neue Mitarbeiter (Schulungen zur Einarbeitung), für externen Partner (Kommunikation)
Das Grafik soll zur Auflockerung mit passenden, leicht verständlichen, jedoch nicht zu vielen, grafischen Elementen angereichert werden.
Die Grafik soll in einer späteren Ausbaustufe auf eigenen Layern zusätzliche Elemente darstellen (z.B. die Teams, die vorhandenen Softwarewerkzeuge oder die verwendeten Dokumente) darstellen.
Als Grafiksoftware sind CorelDraw und Indesign im Betrieb vorhanden. Vorzugsweise soll die Grafik in diesen Formaten zur Verfügung gestellt werden können.

```html
<!DOCTYPE html>
<html lang="de">
<head>
<meta charset="utf-8">
<title>Wertstrom – Lindtal Holzhaus</title>
<link href="https://fonts.googleapis.com/css2?family=Jost:wght@400;500&display=swap" rel="stylesheet">
<style>
:root{
  --blue-top:#1b78c8;
  --blue-bottom:#0a58a6;
  --grey-top:#b0b0b0;
  --grey-bottom:#8f8f8f;
  --green-top:#8cc63f;
  --green-bottom:#3aa335;
  --label-grey:#8a8a8a;
  --label-blue:#0a5fb0;
  --dot:#0a5fb0;
  --rule:#e6e6e6;
  --ink:#1e1e1e;
}
*{margin:0;padding:0;box-sizing:border-box}
html,body{width:1200px;height:1059px;overflow:hidden;background:#fff}
body{font-family:"Jost",sans-serif;position:relative}
.flow{position:absolute;left:0;width:1200px;height:400px}
.flow--arrows{top:0}
.flow--status{top:574px}
.step{position:absolute;height:30px;display:flex;flex-direction:column;align-items:center;justify-content:center;
  color:#fff;font-size:10px;line-height:1.1;text-align:center;font-weight:400;
  background:linear-gradient(var(--blue-top),var(--blue-bottom))}
.flow--status .step{background:linear-gradient(var(--grey-top),var(--grey-bottom))}
.step .code{border-bottom:0.6px solid rgba(255,255,255,.6);padding:0 14px 1px;margin-bottom:1px}
.row-top .step{top:92px}
.row-bottom .step{top:341px}
.tile{position:absolute;top:197px;width:69px;height:69px;color:#fff;display:flex;flex-direction:column;align-items:center;justify-content:center;
  background:linear-gradient(var(--blue-top),var(--blue-bottom));font-size:13.5px;font-weight:500}
.tile svg{margin-bottom:2px}
.flow--status .tile--ok{background:linear-gradient(var(--green-top),var(--green-bottom))}
.mark{position:absolute;transform:translate(-50%,-50%)}
.dot{display:none;width:11px;height:11px;border-radius:50%;background:var(--dot)}
.flow--status .dot{display:block}
.flow--status .chev{display:none}
.chev{stroke:#8a8a8a;fill:none;stroke-width:1.1}
.note{position:absolute;transform:translateX(-50%);font-size:8px;line-height:1.2;color:var(--label-grey);text-align:center;white-space:nowrap}
.flow--status .note{color:var(--label-blue)}
.brand{position:absolute;top:506px;left:0;width:1200px;height:28px}
.brand .rule{position:absolute;top:14px;height:1px;background:var(--rule)}
.brand .name{position:absolute;left:600px;top:0;transform:translateX(-50%);display:flex;align-items:center;gap:7px;
  font-size:19px;font-weight:500;color:var(--ink);letter-spacing:.5px;white-space:nowrap}
.brand .sq{width:12px;height:12px;background:#d3242b}
</style>
</head>
<body>

<svg width="0" height="0" style="position:absolute">
  <defs>
    <g id="chev-right"><path d="M1 1l5 5-5 5M6 1l5 5-5 5"/></g>
  </defs>
</svg>

<!-- two renderings of the same process: arrows, then status points -->
<section class="flow flow--arrows">
  <div class="row-top">
    <div class="step" style="left:119px;width:99px">Marketing</div>
    <div class="step" style="left:292px;width:99px"><span class="code">LIA0001</span>Beratung</div>
    <div class="step" style="left:465px;width:113px">Angebotskalkulation</div>
    <div class="step" style="left:652px;width:103px">Angebots-<br>überarbeitung</div>
    <div class="step" style="left:830px;width:103px">Auftragsklärung /<br>- planung</div>
    <div class="step" style="left:1007px;width:90px">Fertigungs-<br>planung</div>
  </div>
  <div class="row-bottom">
    <div class="step" style="left:119px;width:114px">Fremdleistungen</div>
    <div class="step" style="left:239px;width:78px">Montage</div>
    <div class="step" style="left:394px;width:78px">Transport</div>
    <div class="step" style="left:478px;width:78px">Verladung</div>
    <div class="step" style="left:562px;width:110px"><span class="code">LIA0007</span>Werkstattproduktion</div>
    <div class="step" style="left:677px;width:90px">Material-<br>lieferungen</div>
    <div class="step" style="left:842px;width:91px">Material-<br>lieferungen</div>
    <div class="step" style="left:1007px;width:90px">Liefer-<br>LIA0004</div>
  </div>
  <div class="tile" style="left:119px">
    <svg width="24" height="28" viewBox="0 0 24 28" fill="none" stroke="#fff" stroke-width="1.4"><circle cx="12" cy="7" r="5.5"/><path d="M1.5 27v-3a10.5 9 0 0 1 21 0v3"/></svg>
    Kunde
  </div>
  <div class="tile tile--ok" style="left:1028px">
    <svg width="28" height="18" viewBox="0 0 28 18" fill="none" stroke="#fff" stroke-width="1.6"><path d="M1 9l8 8L27 1"/></svg>
    OK
  </div>

  <!-- connectors -->
  <svg class="mark chev" style="left:255px;top:107px" width="12" height="12"><use href="#chev-right"/></svg>
  <svg class="mark chev" style="left:428px;top:107px" width="12" height="12"><use href="#chev-right"/></svg>
  <svg class="mark chev" style="left:615px;top:107px" width="12" height="12"><use href="#chev-right"/></svg>
  <svg class="mark chev" style="left:793px;top:107px" width="12" height="12"><use href="#chev-right"/></svg>
  <svg class="mark chev" style="left:970px;top:107px" width="12" height="12"><use href="#chev-right"/></svg>
  <svg class="mark chev" style="left:1062px;top:162px;transform:translate(-50%,-50%) rotate(90deg)" width="12" height="12"><use href="#chev-right"/></svg>
  <svg class="mark chev" style="left:1062px;top:304px;transform:translate(-50%,-50%) rotate(90deg)" width="12" height="12"><use href="#chev-right"/></svg>
  <svg class="mark chev" style="left:970px;top:356px;transform:translate(-50%,-50%) rotate(180deg)" width="12" height="12"><use href="#chev-right"/></svg>
  <svg class="mark chev" style="left:805px;top:356px;transform:translate(-50%,-50%) rotate(180deg)" width="12" height="12"><use href="#chev-right"/></svg>
  <svg class="mark chev" style="left:356px;top:356px;transform:translate(-50%,-50%) rotate(180deg)" width="12" height="12"><use href="#chev-right"/></svg>
  <svg class="mark chev" style="left:154px;top:294px;transform:translate(-50%,-50%) rotate(-90deg)" width="12" height="12"><use href="#chev-right"/></svg>
  <svg class="mark chev" style="left:154px;top:146px;transform:translate(-50%,-50%) rotate(-90deg)" width="12" height="12"><use href="#chev-right"/></svg>

  <span class="note" style="left:255px;top:126px">Auftragseingang<br>Architekt</span>
  <span class="note" style="left:428px;top:126px">Anfrageneingang<br>LIA0002</span>
  <span class="note" style="left:615px;top:126px">Angebotsausgang</span>
  <span class="note" style="left:793px;top:126px">Auftragseingang</span>
  <span class="note" style="left:970px;top:126px">LIA0003</span>
  <span class="note" style="left:154px;top:160px">Marktrecherche<br>des Kunden</span>
  <span class="note" style="left:154px;top:308px">Abnahme</span>
  <span class="note" style="left:357px;top:374px">Richttermin</span>
  <span class="note" style="left:805px;top:374px">LIA0006</span>
  <span class="note" style="left:970px;top:374px">LIA0005</span>
</section>

<div class="brand">
  <div class="rule" style="left:15px;width:479px"></div>
  <div class="name"><span class="sq"></span>LINDTAL HOLZHAUS</div>
  <div class="rule" style="left:706px;width:479px"></div>
</div>

<section class="flow flow--status">
  <div class="row-top">
    <div class="step" style="left:119px;width:99px">Marketing</div>
    <div class="step" style="left:292px;width:99px"><span class="code">LIA0001</span>Beratung</div>
    <div class="step" style="left:465px;width:113px">Angebotskalkulation</div>
    <div class="step" style="left:652px;width:103px">Angebots-<br>überarbeitung</div>
    <div class="step" style="left:830px;width:103px">Auftragsklärung /<br>- planung</div>
    <div class="step" style="left:1007px;width:90px">Fertigungs-<br>planung</div>
  </div>
  <div class="row-bottom">
    <div class="step" style="left:119px;width:114px">Fremdleistungen</div>
    <div class="step" style="left:239px;width:78px">Montage</div>
    <div class="step" style="left:394px;width:78px">Transport</div>
    <div class="step" style="left:478px;width:78px">Verladung</div>
    <div class="step" style="left:562px;width:110px"><span class="code">LIA0007</span>Werkstattproduktion</div>
    <div class="step" style="left:677px;width:90px">Material-<br>lieferungen</div>
    <div class="step" style="left:842px;width:91px">Material-<br>lieferungen</div>
    <div class="step" style="left:1007px;width:90px">Liefer-<br>LIA0004</div>
  </div>
  <div class="tile" style="left:119px">
    <svg width="24" height="28" viewBox="0 0 24 28" fill="none" stroke="#fff" stroke-width="1.4"><circle cx="12" cy="7" r="5.5"/><path d="M1.5 27v-3a10.5 9 0 0 1 21 0v3"/></svg>
    Kunde
  </div>
  <div class="tile tile--ok" style="left:1028px">
    <svg width="28" height="18" viewBox="0 0 28 18" fill="none" stroke="#fff" stroke-width="1.6"><path d="M1 9l8 8L27 1"/></svg>
    OK
  </div>

  <span class="mark dot" style="left:255px;top:107px"></span>
  <span class="mark dot" style="left:428px;top:107px"></span>
  <span class="mark dot" style="left:615px;top:107px"></span>
  <span class="mark dot" style="left:793px;top:107px"></span>
  <span class="mark dot" style="left:970px;top:107px"></span>
  <span class="mark dot" style="left:1062px;top:162px"></span>
  <span class="mark dot" style="left:1062px;top:304px"></span>
  <span class="mark dot" style="left:970px;top:356px"></span>
  <span class="mark dot" style="left:805px;top:356px"></span>
  <span class="mark dot" style="left:356px;top:356px"></span>
  <span class="mark dot" style="left:154px;top:294px"></span>
  <span class="mark dot" style="left:154px;top:145px"></span>

  <span class="note" style="left:255px;top:126px">Auftragseingang<br>Architekt</span>
  <span class="note" style="left:428px;top:126px">Anfrageneingang<br>LIA0002</span>
  <span class="note" style="left:615px;top:126px">Angebotsausgang</span>
  <span class="note" style="left:793px;top:126px">Auftragseingang</span>
  <span class="note" style="left:970px;top:126px">LIA0003</span>
  <span class="note" style="left:154px;top:160px">Marktrecherche<br>des Kunden</span>
  <span class="note" style="left:154px;top:308px">Abnahme</span>
  <span class="note" style="left:357px;top:374px">Richttermin</span>
  <span class="note" style="left:805px;top:374px">LIA0006</span>
  <span class="note" style="left:970px;top:374px">LIA0005</span>
</section>

</body>
</html>
```